My website design

It Will be a to-go website for all service requests from the comfort of your home. services ranging from renting an electrician to fix your home electrical issues, DJ for your party, mark-up artist for your wedding and so on. Here are a few websites for inspiration:

https://www.dwellpanel.example/
https://www.chorewren.example/
https://www.gigplover.example/

Number of Pages Required

5+ page

Requirements
Must have
• User's registration form
pros resgistation form
filling out job request form
quotes sent sent back to job requester from various pros within the same zip code
quote accepted
ability to review pros once jobs are completed

```html
<!DOCTYPE html>
<html lang="en">
<head>
<meta charset="utf-8">
<title>Hearthly – Home Services</title>
<link href="https://fonts.googleapis.com/css2?family=Rubik:wght@400;500;600&family=Open+Sans:wght@400;600;700&display=swap" rel="stylesheet">
<style>
:root{
  --green:#2fa843;
  --green-dark:#258a36;
  --ink:#1d1d1d;
  --text:#444;
  --muted:#777;
  --slate:#4a5a63;
  --blush:#f4f0f0;
  --line:#e2e2e2;
  --white:#fff;
}
*{box-sizing:border-box;margin:0;padding:0}
html,body{width:1200px;height:4096px;overflow:hidden}
body{font-family:"Open Sans",sans-serif;color:var(--text);background:var(--white);position:relative}
section,header,footer{position:absolute;left:0;width:1200px}
.abs{position:absolute}
h2{font-family:"Rubik",sans-serif;font-weight:500;color:var(--ink);font-size:24px}
.rule{display:block;width:40px;height:3px;background:var(--ink);margin-top:12px}
.rule.center{margin-left:auto;margin-right:auto}
.btn{display:inline-block;background:var(--green);color:#fff;font-size:14px;font-weight:600;text-transform:uppercase;letter-spacing:.3px;padding:9px 16px}
.btn-outline{display:inline-block;border:2px solid var(--green);color:var(--green);font-size:12px;font-weight:600;text-transform:uppercase;padding:5px 11px}
.tick{width:14px;height:14px;flex:none}

/* header */
.site-header{top:0;height:92px;background:#fff}
.brand{left:132px;top:26px;display:flex;align-items:center;gap:12px}
.brand-square{width:34px;height:34px;background:var(--green)}
.brand-name{font-family:"Open Sans",sans-serif;font-weight:600;font-size:28px;letter-spacing:8px;color:var(--slate)}
.follow{right:130px;top:20px;display:flex;align-items:center;gap:7px;font-size:12px;color:var(--ink)}
.follow .dot{width:22px;height:22px;border-radius:50%;background:#1f4fa0}
.follow .dot.d2{background:#1d91d8}.follow .dot.d3{background:#111}
.follow .btn-outline{margin-left:18px}
.nav{right:132px;top:62px;display:flex;gap:28px;font-size:14px;font-weight:600;color:var(--ink)}
.nav .active{color:var(--green);text-decoration:underline}

/* hero */
.hero{top:92px;height:519px;background:linear-gradient(180deg,#cfd2d1 0%,#b9bdbb 45%,#5f7d80 70%,#c8c3b9 100%)}
.hero-card{left:316px;top:132px;width:570px;height:202px;background:rgba(255,255,255,.9);text-align:center;padding-top:36px}
.hero-card h1{font-family:"Rubik",sans-serif;font-weight:600;font-size:25px;color:var(--ink)}
.hero-card p{font-size:14px;line-height:20px;margin:16px auto 0;width:400px;color:#333}
.search{position:absolute;left:37px;top:130px;width:490px;height:41px;border:1px solid #555;display:flex;background:#fff}
.search .field{flex:1;display:flex;align-items:center;gap:8px;padding-left:14px;font-size:12px;color:#222}
.search .btn{width:150px;height:39px;display:flex;align-items:center;justify-content:center;font-size:14px;font-weight:600}

/* popular */
.popular{top:611px;height:235px;background:#fff}
.popular h2{position:absolute;left:132px;top:34px}
.cats{left:132px;top:107px;width:936px;display:flex}
.cat{flex:1;height:104px;border-right:1px solid var(--line);text-align:center;font-size:12.5px;color:#333}
.cat:last-child{border-right:none}
.cat svg{display:block;margin:12px auto 16px;width:40px;height:40px}

/* area grid */
.area{top:846px;height:636px;background:#fff}
.area h2{text-align:center;margin-top:53px}
.tiles{left:135px;top:149px;width:932px;display:grid;grid-template-columns:repeat(4,226px);grid-auto-rows:207px;gap:10px 9px}
.tile{position:relative;overflow:hidden}
.tile span{position:absolute;left:0;right:0;bottom:0;padding:0 12px 10px;height:56px;display:flex;align-items:flex-end;color:#fff;font-size:13px;font-weight:600;background:linear-gradient(transparent,rgba(0,0,0,.75))}
.t1{background:linear-gradient(135deg,#7a5a3a,#c49a6c)}.t2{background:linear-gradient(135deg,#2d3338,#6f7478)}
.t3{background:linear-gradient(135deg,#45505a,#9fb24a)}.t4{background:linear-gradient(135deg,#35413d,#8ea39a)}
.t5{background:linear-gradient(135deg,#3a2a1e,#d19a3e)}.t6{background:linear-gradient(135deg,#c9b4a4,#6a4a44)}
.t7{background:linear-gradient(135deg,#1c1c1c,#b08a5c)}.t8{background:linear-gradient(135deg,#58503f,#b79f7c)}

/* why */
.why{top:1482px;height:444px;background:var(--blush)}
.why-photo{left:0;top:0;width:604px;height:444px;background:linear-gradient(160deg,#cdd2d5,#7a93b4 55%,#c5bbb0)}
.why-body{left:654px;top:46px;width:400px}
.why-body p{font-size:13px;line-height:19px;margin-top:30px;color:#444}
.checks{list-style:none;margin-top:22px}
.checks li{display:flex;align-items:center;gap:12px;font-size:14px;color:#222;height:27px}
.why-body .btn{margin-top:22px}

/* more */
.more{top:1926px;height:380px;background:#fff}
.more h2{position:absolute;left:132px;top:54px}
.more .btn-outline{position:absolute;right:132px;top:56px}
.col{top:132px;width:220px;list-style:none}
.col li{height:32px;display:flex;align-items:center;gap:12px;padding-left:16px;font-size:13.5px;color:#222;border-bottom:1px solid var(--line)}
.col li:last-child{border-bottom:none}

/* testimonials */
.testimonials{top:2306px;height:408px;background:var(--blush)}
.testimonials h2{text-align:center;margin-top:42px}
.quote{top:122px;width:302px;height:237px;background:#fff;padding:20px 24px 0 24px}
.quote .mark{font-family:Georgia,serif;font-size:38px;color:#bbb;line-height:24px}
.quote p{font-size:12.5px;line-height:17.5px;color:#333;margin:4px 0 0 30px}
.author{position:absolute;left:56px;bottom:20px;display:flex;align-items:center;gap:12px}
.avatar{width:28px;height:28px;border-radius:50%;background:#8d8d8d}
.author b{display:block;font-size:10px;color:#222}
.stars{color:var(--green);font-size:11px;letter-spacing:1px}
.arrow{top:228px}

/* get help */
.help{top:2714px;height:407px;background:var(--slate)}
.help-photo{left:556px;top:0;width:644px;height:407px;background:linear-gradient(120deg,#e9e6e1,#c7bba9 50%,#f2efe9)}
.help-body{left:133px;top:88px;width:340px;color:#fff}
.help-body h2{color:#fff;font-size:30px}
.help-body .rule{background:var(--green)}
.help-body p{font-size:12.5px;line-height:17.5px;margin-top:26px}
.help-body .btn{margin-top:28px}

/* blog */
.blog{top:3121px;height:576px;background:#fff}
.blog h2{text-align:center;margin-top:67px}
.post{top:143px;width:300px;height:374px;background:#fff;box-shadow:0 2px 10px rgba(0,0,0,.12)}
.post .img{height:218px}
.post .body{padding:28px 28px 0}
.post h3{font-size:13.5px;font-weight:700;color:#222}
.post p{font-size:11px;line-height:14.5px;margin-top:12px;color:#444}
.post .btn{font-size:9px;padding:6px 10px;margin-top:12px}
.b1{background:linear-gradient(135deg,#5f6a70,#d0cfc4)}.b2{background:linear-gradient(135deg,#c93bb5,#2d2634)}.b3{background:linear-gradient(135deg,#2e4b7a,#b3b9bf)}

/* footer */
.site-footer{top:3697px;height:399px;background:var(--slate);color:#fff}
.foot-brand{left:134px;top:150px;display:flex;align-items:center;gap:14px}
.foot-brand .sq{width:40px;height:40px;background:#fff}
.foot-brand span{font-size:34px;font-weight:600;letter-spacing:6px}
.foot-col h4{font-family:"Rubik",sans-serif;font-size:16px;font-weight:500;letter-spacing:.5px}
.foot-col ul{list-style:none;margin-top:26px;font-size:14px;line-height:24px}
.contact-row,.social-row{display:flex;gap:14px;font-size:13.5px;line-height:19px;margin-top:20px}
.ico{width:28px;height:28px;border-radius:50%;background:#fff;flex:none;display:flex;align-items:center;justify-content:center}
.copy{left:132px;top:333px;width:936px;border-top:1px solid rgba(255,255,255,.2);padding-top:24px;text-align:center;font-size:12px}
</style>
</head>
<body>

<header class="site-header">
  <div class="abs brand"><span class="brand-square"></span><span class="brand-name">HEARTHLY</span></div>
  <div class="abs follow">FOLLOW US <span class="dot"></span><span class="dot d2"></span><span class="dot d3"></span><span class="btn-outline">Login</span></div>
  <nav class="abs nav"><span class="active">HOME</span><span>ABOUT US</span><span>START A PROJECT</span><span>SERVICES</span><span>CONTACT US</span></nav>
</header>

<section class="hero" role="img" aria-label="Bright living room with teal sofa, rug and pendant lamps">
  <div class="abs hero-card">
    <h1>FIX YOUR HOME ELECTRICAL ISSUES</h1>
    <p>Lorem Ipsum is simply dummy text of the printing and typesetting industry make a type specimen book</p>
    <div class="search">
      <div class="field"><svg width="12" height="12" viewBox="0 0 12 12"><circle cx="5" cy="5" r="3.6" fill="none" stroke="#222" stroke-width="1.5"/><path d="M7.6 7.6L11 11" stroke="#222" stroke-width="1.5"/></svg>I need help with</div>
      <span class="btn">Get help today</span>
    </div>
  </div>
</section>

<section class="popular">
  <h2>Most Popular Projects<span class="rule"></span></h2>
  <div class="abs cats">
    <div class="cat"><svg viewBox="0 0 40 40" fill="none" stroke="var(--green)" stroke-width="1.6"><rect x="3" y="20" width="34" height="14"/><rect x="25" y="8" width="12" height="12"/><path d="M8 20v-8h6v8M11 12V6M3 27h22"/></svg>Kitchen Remodel</div>
    <div class="cat"><svg viewBox="0 0 40 40" fill="none" stroke="var(--green)" stroke-width="1.6"><path d="M3 20h34v4a9 9 0 0 1-9 9H12a9 9 0 0 1-9-9z"/><path d="M8 20V9a3 3 0 0 1 6 0M12 33l-2 4M28 33l2 4M20 13l3-3 5 5"/></svg>Bathroom Remodel</div>
    <div class="cat"><svg viewBox="0 0 40 40" fill="none" stroke="var(--green)" stroke-width="1.6"><rect x="3" y="8" width="34" height="14" rx="2"/><path d="M7 17h26M12 26v8M20 26v8M28 26v8"/></svg>Heating &amp; Cooling</div>
    <div class="cat"><svg viewBox="0 0 40 40" fill="none" stroke="var(--green)" stroke-width="1.6"><path d="M14 4v9M26 4v9M11 13h18v7a9 9 0 0 1-18 0zM20 29v8"/></svg>Electrical Services</div>
    <div class="cat"><svg viewBox="0 0 40 40" fill="none" stroke="var(--green)" stroke-width="1.6"><rect x="6" y="4" width="28" height="32"/><path d="M20 4v32M6 20h28"/></svg>Windows &amp; Doors</div>
    <div class="cat"><svg viewBox="0 0 40 40" fill="var(--green)"><path d="M2 30l12-14 12 14h-6l-6-7-6 7zM18 30l12-14 8 14h-6l-2-4-2 4z"/></svg>Roofing &amp; Gutters</div>
  </div>
</section>

<section class="area">
  <h2>Popular projects in your area<span class="rule center"></span></h2>
  <div class="abs tiles">
    <div class="tile t1" role="img" aria-label="Sanding a wooden tabletop"><span>Assemble a Table/Desk</span></div>
    <div class="tile t2" role="img" aria-label="Wall mount bracket for a TV"><span>Mount a TV or Mirror</span></div>
    <div class="tile t3" role="img" aria-label="Gloved hand cleaning a kitchen sink"><span>Clean kitchen</span></div>
    <div class="tile t4" role="img" aria-label="Electrician working at a fuse panel"><span>Electrical Work</span></div>
    <div class="tile t5" role="img" aria-label="DJ mixing deck under warm lights"><span>DJ Party</span></div>
    <div class="tile t6" role="img" aria-label="Make-up being applied"><span>Mount a TV or Mirror</span></div>
    <div class="tile t7" role="img" aria-label="Paper delivery bag"><span>Home Delivery</span></div>
    <div class="tile t8" role="img" aria-label="Movers loading boxes into a truck"><span>Move Boxes via Truck</span></div>
  </div>
</section>

<section class="why">
  <div class="abs why-photo" role="img" aria-label="Electrician fitting a ceiling light"></div>
  <div class="abs why-body">
    <h2>Why Choose us<span class="rule"></span></h2>
    <p>There are many variations of passages of Lorem Ipsum available, but the majority have suffered alteration in some form, by injected humour, or randomised words.</p>
    <ul class="checks">
      <li><svg class="tick" viewBox="0 0 14 14"><path d="M2 7.5l3 3 7-7" fill="none" stroke="var(--green)" stroke-width="2.4"/></svg>It is a long established fact</li>
      <li><svg class="tick" viewBox="0 0 14 14"><path d="M2 7.5l3 3 7-7" fill="none" stroke="var(--green)" stroke-width="2.4"/></svg>Lorem Ipsum is simply dummy</li>
      <li><svg class="tick" viewBox="0 0 14 14"><path d="M2 7.5l3 3 7-7" fill="none" stroke="var(--green)" stroke-width="2.4"/></svg>But I must explain to you how</li>
      <li><svg class="tick" viewBox="0 0 14 14"><path d="M2 7.5l3 3 7-7" fill="none" stroke="var(--green)" stroke-width="2.4"/></svg>At vero eos et accusamus</li>
      <li><svg class="tick" viewBox="0 0 14 14"><path d="M2 7.5l3 3 7-7" fill="none" stroke="var(--green)" stroke-width="2.4"/></svg>Lorem ipsum dolor sit amet</li>
    </ul>
    <span class="btn">Read more</span>
  </div>
</section>

<section class="more">
  <h2>More Projects<span class="rule"></span></h2>
  <span class="btn-outline">View all categories</span>
  <ul class="abs col" style="left:132px">
    <li><svg class="tick" viewBox="0 0 14 14"><path d="M2 7.5l3 3 7-7" fill="none" stroke="var(--green)" stroke-width="2.4"/></svg>Additions &amp; Remodels</li>
    <li><svg class="tick" viewBox="0 0 14 14"><path d="M2 7.5l3 3 7-7" fill="none" stroke="var(--green)" stroke-width="2.4"/></svg>Cabinets &amp; Countertops</li>
    <li><svg class="tick" viewBox="0 0 14 14"><path d="M2 7.5l3 3 7-7" fill="none" stroke="var(--green)" stroke-width="2.4"/></svg>Cleaning &amp; Maid Service</li>
    <li><svg class="tick" viewBox="0 0 14 14"><path d="M2 7.5l3 3 7-7" fill="none" stroke="var(--green)" stroke-width="2.4"/></svg>Electrical &amp; Computers</li>
    <li><svg class="tick" viewBox="0 0 14 14"><path d="M2 7.5l3 3 7-7" fill="none" stroke="var(--green)" stroke-width="2.4"/></svg>Handyman Services</li>
    <li><svg class="tick" viewBox="0 0 14 14"><path d="M2 7.5l3 3 7-7" fill="none" stroke="var(--green)" stroke-width="2.4"/></svg>Remodels</li>
  </ul>
  <ul class="abs col" style="left:494px">
    <li><svg class="tick" viewBox="0 0 14 14"><path d="M2 7.5l3 3 7-7" fill="none" stroke="var(--green)" stroke-width="2.4"/></svg>Appliances</li>
    <li><svg class="tick" viewBox="0 0 14 14"><path d="M2 7.5l3 3 7-7" fill="none" stroke="var(--green)" stroke-width="2.4"/></svg>Carpentry</li>
    <li><svg class="tick" viewBox="0 0 14 14"><path d="M2 7.5l3 3 7-7" fill="none" stroke="var(--green)" stroke-width="2.4"/></svg>Driveways, Patios &amp; Walks</li>
    <li><svg class="tick" viewBox="0 0 14 14"><path d="M2 7.5l3 3 7-7" fill="none" stroke="var(--green)" stroke-width="2.4"/></svg>Fences</li>
    <li><svg class="tick" viewBox="0 0 14 14"><path d="M2 7.5l3 3 7-7" fill="none" stroke="var(--green)" stroke-width="2.4"/></svg>Lawncare &amp; Sprinklers</li>
    <li><svg class="tick" viewBox="0 0 14 14"><path d="M2 7.5l3 3 7-7" fill="none" stroke="var(--green)" stroke-width="2.4"/></svg>Tile &amp; Stone</li>
  </ul>
  <ul class="abs col" style="left:840px">
    <li><svg class="tick" viewBox="0 0 14 14"><path d="M2 7.5l3 3 7-7" fill="none" stroke="var(--green)" stroke-width="2.4"/></svg>Architects &amp; Engineers</li>
    <li><svg class="tick" viewBox="0 0 14 14"><path d="M2 7.5l3 3 7-7" fill="none" stroke="var(--green)" stroke-width="2.4"/></svg>Carpet</li>
    <li><svg class="tick" viewBox="0 0 14 14"><path d="M2 7.5l3 3 7-7" fill="none" stroke="var(--green)" stroke-width="2.4"/></svg>Drywall &amp; Insulation</li>
    <li><svg class="tick" viewBox="0 0 14 14"><path d="M2 7.5l3 3 7-7" fill="none" stroke="var(--green)" stroke-width="2.4"/></svg>Garages, Doors, Openers</li>
    <li><svg class="tick" viewBox="0 0 14 14"><path d="M2 7.5l3 3 7-7" fill="none" stroke="var(--green)" stroke-width="2.4"/></svg>Plumbing</li>
    <li><svg class="tick" viewBox="0 0 14 14"><path d="M2 7.5l3 3 7-7" fill="none" stroke="var(--green)" stroke-width="2.4"/></svg>Walls &amp; Ceilings</li>
  </ul>
</section>

<section class="testimonials">
  <h2>Client Testimonials</h2>
  <svg class="abs arrow" style="left:84px" width="14" height="22" viewBox="0 0 14 22"><path d="M11 2L3 11l8 9" fill="none" stroke="#999" stroke-width="2"/></svg>
  <div class="abs quote" style="left:132px"><div class="mark">&ldquo;</div><p>There are many variations of passages of Lorem Ipsum available, but the majority have suffered alteration in some form, by injected humour, or randomised words.eos qui ratione volu ptatem sequi nesciun.</p><div class="author"><span class="avatar"></span><div><b>ROWAN</b><span class="stars">★★★★★</span></div></div></div>
  <div class="abs quote" style="left:450px"><div class="mark">&ldquo;</div><p>At vero eos et accusamus et iusto odio dignissimos ducimus qui blanditiis praesentium voluptatum deleniti atque corrupti quos dolo res et quas molestias excep turi sint occaecati cupiditate non provident, similique sun.</p><div class="author"><span class="avatar"></span><div><b>ROWAN</b><span class="stars">★★★★★</span></div></div></div>
  <div class="abs quote" style="left:765px"><div class="mark">&ldquo;</div><p>On the other hand, we denounce with righteous indignation and dislike men who are so beguiled and demoralized by the charms of pleasure of the moment, so blinded by desirethat they cannot foresee the pain .</p><div class="author"><span class="avatar"></span><div><b>ROWAN</b><span class="stars">★★★★★</span></div></div></div>
  <svg class="abs arrow" style="left:1106px" width="14" height="22" viewBox="0 0 14 22"><path d="M3 2l8 9-8 9" fill="none" stroke="#999" stroke-width="2"/></svg>
</section>

<section class="help">
  <div class="abs help-body">
    <h2>Get Help Today<span class="rule"></span></h2>
    <p>There are many variations of passages of Lorem Ipsum available, but the majority have suffered alteration in some form, by injected humour, or randomised ords. eos qui ratione volu ptatem sequi nesciun.</p>
    <span class="btn">Get started</span>
  </div>
  <div class="abs help-photo" role="img" aria-label="Cleaner wiping a wooden shelf"></div>
</section>

<section class="blog">
  <h2>Latest Blog<span class="rule center"></span></h2>
  <article class="abs post" style="left:134px"><div class="img b1" role="img" aria-label="Electrician testing a circuit panel"></div><div class="body"><h3>At vero eos et accusamus et iusto</h3><p>There are many variations of passages of Lorem Ipsum available, but the majority have suffered alteration in some form.</p><span class="btn">Read more</span></div></article>
  <article class="abs post" style="left:450px"><div class="img b2" role="img" aria-label="DJ deck under pink lights"></div><div class="body"><h3>At vero eos et accusamus et iusto</h3><p>There are many variations of passages of Lorem Ipsum available, but the majority have suffered alteration in some form.</p><span class="btn">Read more</span></div></article>
  <article class="abs post" style="left:768px"><div class="img b3" role="img" aria-label="Electrician wiring a distribution board"></div><div class="body"><h3>At vero eos et accusamus et iusto</h3><p>There are many variations of passages of Lorem Ipsum available, but the majority have suffered alteration in some form.</p><span class="btn">Read more</span></div></article>
</section>

<footer class="site-footer">
  <div class="abs foot-brand"><span class="sq"></span><span>HEARTHLY</span></div>
  <div class="abs foot-col" style="left:439px;top:60px"><h4>MENU</h4><ul><li>HOME</li><li>ABOUT US</li><li>START A PROJECT</li><li>SERVICES</li><li>LOGIN</li></ul></div>
  <div class="abs foot-col" style="left:642px;top:60px;width:260px"><h4>CONTACT US</h4>
    <div class="contact-row" style="margin-top:24px"><span class="ico"><svg width="12" height="14" viewBox="0 0 12 14"><path d="M6 13S1 8 1 5a5 5 0 0 1 10 0c0 3-5 8-5 8z" fill="var(--slate)"/><circle cx="6" cy="5" r="1.8" fill="#fff"/></svg></span><span>Unit 4, Larkspur Works<br>Millbrook Yard<br>Harlow Bay HB7 2QX</span></div>
    <div class="contact-row"><span class="ico"><svg width="14" height="14" viewBox="0 0 14 14"><path d="M3 1l3 3-2 2a8 8 0 0 0 4 4l2-2 3 3-2 2C6 13 1 8 1 3z" fill="var(--slate)"/></svg></span><span style="line-height:28px">555.014.2290</span></div>
    <div class="contact-row"><span class="ico"><svg width="14" height="10" viewBox="0 0 14 10"><rect width="14" height="10" fill="var(--slate)"/><path d="M0 0l7 5 7-5" fill="none" stroke="#fff"/></svg></span><span style="line-height:28px">hello@hearthly.example</span></div>
  </div>
  <div class="abs foot-col" style="left:933px;top:60px;width:160px"><h4>FOLLOW US</h4>
    <div class="social-row" style="margin-top:24px"><span class="ico"></span><span>Like us on<br>FRIENDNEST</span></div>
    <div class="social-row"><span class="ico"></span><span>Follow us on<br>CHIRPLINE</span></div>
    <div class="social-row"><span class="ico"></span><span>Follow us on<br>WORKWEAVE</span></div>
  </div>
  <div class="abs copy">Copyright © 2020 All Rights Reserved</div>
</footer>

</body>
</html>
```